Medical Aesthetics business cards

Looking for a business card for my new medical aesthetics business. I am a nurse practitioner and will be administering quilen , fillers as well as providing other services

```html
<!DOCTYPE html>
<html lang="en">
<head>
<meta charset="utf-8">
<title>Lumen Aesthetics – Business Card</title>
<link href="https://fonts.googleapis.com/css2?family=Questrial&display=swap" rel="stylesheet">
<style>
  :root {
    --plum: #951c55;
    --plum-deep: #4a1f31;
    --magenta: #c91f6d;
    --bleed-grey: #5b5658;
    --white: #ffffff;
    --skin-light: #f6ddd2;
    --skin-mid: #e9bfae;
    --lip-pink: #e59aa6;
  }
  html, body {
    margin: 0;
    width: 1200px;
    height: 720px;
    overflow: hidden;
    background: #ffffff;
  }
  .card-sheet {
    display: block;
    width: 1200px;
    height: 720px;
  }
  .brand-name { font-family: "Questrial", sans-serif; font-size: 56px; fill: var(--plum); }
  .holder-name { font-family: "Questrial", sans-serif; font-size: 31px; fill: var(--white); }
  .holder-role { font-family: "Questrial", sans-serif; font-size: 22px; fill: var(--white); }
  .contact-line { font-family: "Questrial", sans-serif; font-size: 25px; fill: var(--white); }
  .web-line { font-family: "Questrial", sans-serif; font-size: 23px; fill: var(--white); }
  .bleed-label { font-family: "Questrial", sans-serif; font-size: 24px; letter-spacing: 4px; fill: var(--white); }
  .guide-arrow { stroke: var(--white); stroke-width: 3; fill: none; }
  .icon-ring { fill: none; stroke: var(--white); stroke-width: 2; }
</style>
</head>
<body>
<svg class="card-sheet" viewBox="0 0 1125 675" xmlns="http://www.w3.org/2000/svg">
  <defs>
    <linearGradient id="bleed-shade" x1="0" y1="0" x2="0" y2="1">
      <stop offset="0" stop-color="#5f5a5c"/>
      <stop offset="0.6" stop-color="#5a4a50"/>
      <stop offset="0.7" stop-color="#4a1f31"/>
      <stop offset="1" stop-color="#4a1f31"/>
    </linearGradient>
    <linearGradient id="portrait-tone" x1="0" y1="0" x2="1" y2="0.2">
      <stop offset="0" stop-color="#f3d6ca"/>
      <stop offset="0.45" stop-color="#eec6b6"/>
      <stop offset="0.75" stop-color="#f7e4dc"/>
      <stop offset="1" stop-color="#ffffff"/>
    </linearGradient>
    <clipPath id="card-trim">
      <rect x="37" y="37" width="1051" height="600" rx="30"/>
    </clipPath>
  </defs>

  <!-- bleed frame -->
  <rect class="bleed-frame" x="0" y="0" width="1125" height="675" rx="42" fill="url(#bleed-shade)"/>

  <!-- trimmed card -->
  <g clip-path="url(#card-trim)">
    <rect x="37" y="37" width="1051" height="600" fill="var(--white)"/>
    <rect class="portrait-area" x="37" y="37" width="700" height="520" fill="url(#portrait-tone)"
          role="img" aria-label="Beauty photograph: close-up of a woman's lips, chin and manicured hand"/>
    <path class="wave-accent" d="M37 415 C150 470 250 520 420 470 C600 420 780 355 940 358 L940 372 C780 372 600 440 420 495 C250 545 140 500 37 455 Z" fill="var(--magenta)"/>
    <path class="wave-band" d="M37 478 C160 540 260 565 430 520 C620 470 850 365 1088 390 L1088 637 L37 637 Z" fill="var(--plum)"/>
  </g>

  <!-- brand -->
  <circle class="brand-mark" cx="845" cy="160" r="72" fill="var(--plum)"/>
  <text class="brand-name" x="1035" y="303" text-anchor="end">Lumen Aesthetics</text>

  <!-- card holder -->
  <text class="holder-name" x="1035" y="470" text-anchor="end">Dana Morrow, APRN-C</text>
  <text class="holder-role" x="1035" y="501" text-anchor="end">Nurse Practitioner</text>

  <!-- contact -->
  <text class="contact-line" x="985" y="555" text-anchor="end">555-014-2290</text>
  <circle class="icon-ring" cx="1020" cy="546" r="15"/>
  <path class="phone-icon" d="M1014 538 q-3 3 0 9 q4 7 10 8 l3 -3 l-4 -4 l-2 2 q-4 -2 -5 -6 l2 -2 l-3 -4 Z" fill="var(--white)"/>
  <text class="contact-line" x="985" y="593" text-anchor="end">hello@lumenaesthetics.com</text>
  <circle class="icon-ring" cx="1020" cy="585" r="15"/>
  <rect x="1011" y="579" width="18" height="12" fill="var(--white)"/>
  <polyline points="1011,579 1020,587 1029,579" fill="none" stroke="var(--plum)" stroke-width="1.5"/>

  <text class="web-line" x="87" y="593">www.lumenaesthetics.com</text>

  <!-- bleed guides -->
  <text class="bleed-label" x="562" y="27" text-anchor="middle">bleed area</text>
  <text class="bleed-label" x="562" y="664" text-anchor="middle">bleed area</text>
  <text class="bleed-label" transform="translate(27 337) rotate(-90)" text-anchor="middle">bleed area</text>
  <text class="bleed-label" transform="translate(1095 337) rotate(90)" text-anchor="middle">bleed area</text>

  <path class="guide-arrow" d="M370 17 H288 M298 10 L288 17 L298 24"/>
  <path class="guide-arrow" d="M740 17 H822 M812 10 L822 17 L812 24"/>
  <path class="guide-arrow" d="M370 656 H288 M298 649 L288 656 L298 663"/>
  <path class="guide-arrow" d="M740 656 H822 M812 649 L822 656 L812 663"/>
  <path class="guide-arrow" d="M18 210 V140 M11 150 L18 140 L25 150"/>
  <path class="guide-arrow" d="M18 475 V555 M11 545 L18 555 L25 545"/>
  <path class="guide-arrow" d="M1104 210 V130 M1097 140 L1104 130 L1111 140"/>
  <path class="guide-arrow" d="M1104 475 V555 M1097 545 L1104 555 L1111 545"/>
</svg>
</body>
</html>
```